Update Law Firm Website

Update law firm website pages, add pages for employees. Current website looks stale. www.vantholmlegal.example

Target Market(s)

Personal injury clients

Industry/Entity Type

Legal

Number of Pages Required

5+ page

Font styles to use
Serif

Requirements
Must have
• User friendly and engaging design
Nice to have
• ?
Should not have
• scales of justice, law books,

```html
<!DOCTYPE html>
<html lang="en">
<head>
<meta charset="utf-8">
<title>Vantholm Injury Law Group</title>
<link href="https://fonts.googleapis.com/css2?family=Tinos:ital,wght@0,400;0,700;1,400&family=Cinzel:wght@400;600&display=swap" rel="stylesheet">
<style>
:root{
  --maroon:#6a0808;
  --maroon-dark:#560404;
  --gold:#b7811f;
  --gold-light:#d39c2c;
  --ink:#2b2b2b;
  --text:#3a3a3a;
  --mist:#ececec;
  --white:#ffffff;
  --line:#d6d6d6;
}
*{margin:0;padding:0;box-sizing:border-box}
html,body{width:1200px;height:2922px;overflow:hidden}
body{position:relative;font-family:"Tinos",Georgia,serif;color:var(--text);background:var(--white)}
.abs{position:absolute}
.gold{color:var(--gold)}

/* header */
.site-header{position:absolute;left:0;top:0;width:1200px;height:107px;background:var(--white)}
.brand{position:absolute;left:100px;top:22px}
.brand-name{font-size:27px;color:var(--maroon);line-height:1.1}
.brand-sub{font-size:14px;color:var(--gold);letter-spacing:.5px;margin-top:4px}
.contact-chip{position:absolute;top:30px;display:flex;gap:12px;align-items:flex-start}
.contact-chip .label{font-size:14px;color:var(--maroon)}
.contact-chip .value{font-size:13px;color:var(--ink);margin-top:2px}
.chip-icon{width:36px;height:36px;border:2px solid var(--gold);border-radius:50%;display:flex;align-items:center;justify-content:center}

/* nav */
.main-nav{position:absolute;left:0;top:107px;width:1200px;height:45px;background:var(--maroon-dark);border-top:2px solid #8d1a12}
.main-nav ul{list-style:none;display:flex;position:absolute;left:100px;top:0;height:43px}
.main-nav li{font-size:15px;color:var(--white);padding:0 19px;line-height:43px;border-right:1px solid #7a1a14}
.main-nav li.active{background:var(--gold);padding:0 26px}
.main-nav li:last-child{border-right:none}

/* hero */
.hero{position:absolute;left:0;top:152px;width:1200px;height:471px;background:linear-gradient(100deg,#2a1a10 0%,#5a3d24 28%,#3b3b42 55%,#1f2230 80%,#8a6a48 100%)}
.hero-copy{position:absolute;left:100px;top:128px;font-size:22px;line-height:34px;color:var(--white)}
.hero-copy .caps{font-family:"Cinzel",serif;font-size:21px}
.hero-band{position:absolute;left:0;top:338px;width:1200px;height:66px;background:linear-gradient(90deg,rgba(255,255,255,0) 0%,rgba(255,255,255,.78) 20%,rgba(255,255,255,.78) 80%,rgba(255,255,255,0) 100%)}
.hero-band p{font-family:"Cinzel",serif;font-weight:600;font-size:23px;color:#262626;text-align:center;line-height:66px;letter-spacing:.6px}
.hero-dots{position:absolute;left:572px;top:427px;display:flex;gap:6px}
.hero-dots span{width:11px;height:11px;border-radius:50%;background:#aaa}
.hero-dots span.on{background:var(--white);border:2px solid #666}

/* section headings */
.section-title{position:absolute;left:0;width:1200px;text-align:center;font-size:32px;color:var(--ink)}
.section-title::after{content:"";display:block;width:60px;height:2px;background:var(--gold);margin:8px auto 0}

/* cases */
.cases{position:absolute;left:0;top:623px;width:1200px;height:308px;background:var(--white)}
.case-list{position:absolute;left:100px;top:125px;width:1000px;display:flex;justify-content:space-between}
.case{width:150px;text-align:center;font-size:15px;color:var(--ink)}
.case .icon{width:100px;height:100px;border-radius:50%;margin:0 auto 14px;background:#f4f4f4;border:4px solid #e2e2e2;box-shadow:0 2px 6px rgba(0,0,0,.15)}
.case .icon.active{background:var(--maroon);border-color:#e6d6d6}
.case-arrow{position:absolute;top:160px;font-size:34px;color:#c9a27a}

/* welcome */
.welcome{position:absolute;left:0;top:931px;width:1200px;height:439px;background:linear-gradient(180deg,#e9e9e9,#f2f2f2)}
.welcome-title{position:absolute;left:100px;top:57px;font-size:31px;color:var(--maroon)}
.portrait{position:absolute;left:100px;top:130px;width:140px;height:170px;background:linear-gradient(160deg,#8c6c5a,#3a2c28 70%,#1e1e24);border:5px solid var(--white);box-shadow:0 1px 4px rgba(0,0,0,.25)}
.badge{position:absolute;left:100px;top:303px;width:140px;height:38px;background:var(--gold);border-radius:3px}
.welcome-text{position:absolute;left:253px;top:130px;width:475px;font-size:13.5px;line-height:23px;text-align:justify}
.welcome-text p+p{margin-top:10px}
.btn{position:absolute;background:var(--maroon);color:var(--white);font-size:13px;text-align:center;letter-spacing:.5px;border-bottom:3px solid #3e0202;border-radius:2px}
.consult{position:absolute;left:758px;top:75px;width:342px;height:245px;background:var(--white);border:1px solid var(--line)}
.consult-tab{position:absolute;left:38px;top:-14px;width:264px;height:40px;background:var(--maroon);color:var(--white);text-align:center;line-height:40px;font-size:18px}
.field{position:absolute;left:20px;width:300px;height:32px;background:#ebebeb;border:1px solid #d9d9d9;border-radius:3px;font-size:13px;color:#777;padding:7px 10px}
.field b{color:#c21a1a;font-weight:400}

/* liability */
.liability{position:absolute;left:0;top:1370px;width:1200px;height:442px;background:linear-gradient(180deg,var(--maroon) 0%,var(--maroon) 66%,#e4e4e4 66%,#f4f4f4 100%)}
.liability .section-title{color:var(--white);top:28px}
.basis{position:absolute;top:95px;width:270px;text-align:center}
.basis .icon{width:90px;height:90px;border-radius:50%;background:var(--white);border:5px solid #8d2a22;margin:0 auto;display:flex;align-items:center;justify-content:center}
.basis h3{font-weight:400;font-size:17px;color:var(--gold-light);margin-top:30px}
.basis .card{position:relative;margin-top:14px;background:var(--white);height:140px;padding:14px 16px;font-size:13px;line-height:19px;color:var(--ink);box-shadow:0 3px 10px rgba(0,0,0,.18)}
.basis .plus{position:absolute;left:118px;bottom:-12px;width:34px;height:24px;border-radius:17px 17px 0 0;background:var(--gold);color:var(--white);font-size:18px;line-height:26px}

/* compensation */
.compensation{position:absolute;left:0;top:1812px;width:1200px;height:497px;background:#f1f1f1}
.comp-visual{position:absolute;left:600px;top:0;width:600px;height:497px;background:linear-gradient(90deg,#f1f1f1 0%,#dcdcdc 25%,#cfcfcf 60%,#8a6a48 100%)}
.comp-title{position:absolute;left:100px;top:50px;font-size:29px;line-height:36px;color:var(--maroon)}
.comp-text{position:absolute;left:100px;top:150px;width:540px;font-size:13.5px;line-height:22px;text-align:justify}
.comp-text p+p{margin-top:10px}
.damages{position:absolute;left:100px;top:377px;width:600px;display:grid;grid-template-columns:200px 228px 172px;row-gap:9px;font-size:13.5px}
.damages span{display:flex;align-items:center;gap:8px}

/* attorneys */
.attorneys{position:absolute;left:0;top:2309px;width:1200px;height:298px;background:var(--white)}
.attorneys .section-title{top:42px;color:var(--maroon)}
.attorneys h4{position:absolute;left:0;top:118px;width:1200px;text-align:center;font-weight:400;font-size:18px;color:#111}
.attorneys p{position:absolute;left:100px;top:150px;width:1000px;text-align:center;font-size:13.5px;line-height:22px}

/* footer */
.site-footer{position:absolute;left:0;top:2607px;width:1200px;height:273px;background:var(--maroon)}
.foot-head{position:absolute;top:45px;font-size:15px;color:var(--white);letter-spacing:.5px}
.foot-rule{position:absolute;top:72px;height:1px;background:#8d2a22}
.foot-links{position:absolute;top:95px;list-style:none;font-size:13.5px;color:var(--white)}
.foot-links li{height:40px}
.foot-links li::before{content:"› ";color:var(--gold-light)}
.foot-contact{position:absolute;left:492px;top:92px;font-size:13px;color:var(--white);line-height:19px}
.foot-contact .row{display:flex;gap:10px;margin-bottom:10px}
.foot-brand{position:absolute;left:720px;top:80px;width:380px;text-align:center}
.foot-brand .name{font-size:26px;color:var(--white)}
.foot-brand .sub{font-size:14px;color:var(--gold-light);margin-top:12px;letter-spacing:.5px}
.social{display:flex;gap:12px;justify-content:center;margin-top:40px}
.social span{width:32px;height:32px;border-radius:50%;background:var(--white)}
.copyright{position:absolute;left:0;top:2880px;width:1200px;height:42px;background:var(--gold);color:var(--white);font-size:13px;text-align:center;line-height:42px}
</style>
</head>
<body>

<header class="site-header">
  <div class="brand">
    <div class="brand-name">Vantholm Injury Law Group</div>
    <div class="brand-sub">DANIEL R. VANTHOLM, ESQUIRE</div>
  </div>
  <div class="contact-chip" style="left:650px">
    <div class="chip-icon"><svg width="18" height="18" viewBox="0 0 24 24"><path d="M6.6 10.8a15 15 0 0 0 6.6 6.6l2.2-2.2c.3-.3.7-.4 1-.2 1.1.4 2.3.6 3.6.6.6 0 1 .4 1 1V20c0 .6-.4 1-1 1A17 17 0 0 1 3 4c0-.6.4-1 1-1h3.5c.6 0 1 .4 1 1 0 1.3.2 2.5.6 3.6.1.3 0 .7-.2 1z" fill="#b7811f"/></svg></div>
    <div><div class="label">Call Us:</div><div class="value">(555) 014-2270 / (555) 014-3381</div></div>
  </div>
  <div class="contact-chip" style="left:913px">
    <div class="chip-icon"><svg width="18" height="14" viewBox="0 0 24 18"><rect x="1" y="1" width="22" height="16" fill="none" stroke="#b7811f" stroke-width="2"/><path d="M1 1l11 9 11-9" fill="none" stroke="#b7811f" stroke-width="2"/></svg></div>
    <div><div class="label">Mail Us:</div><div class="value">inquiry@vantholmlegal.example</div></div>
  </div>
</header>

<nav class="main-nav">
  <ul>
    <li class="active">Home</li><li>Slip and Fall</li><li>Auto Accident</li><li>Construction Injuries</li><li>Medical Malpractice</li><li>Results</li><li>About Us</li><li>Contact Us</li>
  </ul>
</nav>

<section class="hero" role="img" aria-label="Attorney in a suit signing documents at a desk">
  <div class="hero-copy">We take all cases on a contingency basis,<br>meaning you will not pay attorney fees or costs<br>unless <span class="caps">WE RECOVER ON YOUR BEHALF.</span></div>
  <div class="hero-band"><p>AFFORDABLE AND ESSENTIAL LEGAL ADVOCATE FOR YOUR INJURY CLAIM</p></div>
  <div class="hero-dots"><span class="on"></span><span></span><span></span><span></span></div>
</section>

<section class="cases">
  <h2 class="section-title" style="top:38px;font-weight:400">Personal <span class="gold">Injury Cases</span></h2>
  <div class="case-arrow" style="left:82px">‹</div>
  <div class="case-arrow" style="left:1100px">›</div>
  <div class="case-list">
    <div class="case"><div class="icon" role="img" aria-label="Pipeline explosion icon"></div>Pipeline Explosions</div>
    <div class="case"><div class="icon" role="img" aria-label="Dog bite icon"></div>Dog Bites</div>
    <div class="case"><div class="icon active" role="img" aria-label="Car accident icon"></div>Car Accidents</div>
    <div class="case"><div class="icon" role="img" aria-label="Defective product icon"></div>Defective Products</div>
    <div class="case"><div class="icon" role="img" aria-label="Vehicle collision icon"></div>Collisions</div>
    <div class="case"><div class="icon" role="img" aria-label="Slip and fall icon"></div>Slip And Fall</div>
  </div>
</section>

<section class="welcome">
  <h2 class="welcome-title" style="font-weight:400">Welcome To <span class="gold">Vantholm Injury Law Group</span></h2>
  <div class="portrait" role="img" aria-label="Portrait of the attorney"></div>
  <div class="badge" role="img" aria-label="Recognition badge"></div>
  <div class="welcome-text">
    <p>Daniel R. Vantholm is a Philadelphia Injury Lawyer who has successfully handled death and serious injury cases involving city transit, car and trucking accidents, injuries caused by toxic chemicals, slip and fall cases involving shopping centers and office buildings, and against insurance companies.</p>
    <p>When you are hit by a fatigued driver of a tractor-trailer or you suffer a fatal stroke because of a delayed diagnosis by a physician, the consequences can include staggering medical bills, debilitating pain and permanent disability. While overcoming the emotional, physical and financial hardships...</p>
  </div>
  <div class="btn" style="left:418px;top:337px;width:130px;height:36px;line-height:33px">READ MORE</div>
  <form class="consult">
    <div class="consult-tab">Free Consultation Form</div>
    <div class="field" style="top:40px">Name<b>*</b></div>
    <div class="field" style="top:80px">Email<b>*</b></div>
    <div class="field" style="top:120px">Phone<b>*</b></div>
    <div class="field" style="top:160px">Case<b>*</b></div>
    <div class="field" style="top:200px">Message<b>*</b></div>
    <div class="btn" style="left:103px;top:258px;width:130px;height:36px;line-height:33px">SUBMIT</div>
  </form>
</section>

<section class="liability">
  <h2 class="section-title" style="font-weight:400">Basis for <span class="gold" style="color:var(--gold-light)">Imposing Liability</span></h2>
  <div class="basis" style="left:91px">
    <div class="icon"><svg width="40" height="40" viewBox="0 0 40 40"><circle cx="20" cy="12" r="8" fill="#2b2b2b"/><path d="M5 38c0-9 7-15 15-15s15 6 15 15z" fill="#2b2b2b"/></svg></div>
    <h3>Negligence &amp; Recklessness</h3>
    <div class="card">Most personal injury claims are based on the law of negligence. In basic term, negligence refers to the failure of a party to act with reasonable care which causes foreseeable injury toward..<div class="plus">+</div></div>
  </div>
  <div class="basis" style="left:465px">
    <div class="icon"><svg width="40" height="40" viewBox="0 0 40 40"><rect x="6" y="5" width="24" height="30" rx="2" fill="none" stroke="#2b2b2b" stroke-width="3"/><path d="M11 13h14M11 19h14M11 25h8" stroke="#2b2b2b" stroke-width="2.5"/><path d="M24 30l12-12 3 3-12 12h-3z" fill="#2b2b2b"/></svg></div>
    <h3>Intentional Actions</h3>
    <div class="card">When a party commits a physical assault, battery, rape, sexual assault or other form of intentional conduct that causes injury, this type of case is referred to as an intentional tort..<div class="plus">+</div></div>
  </div>
  <div class="basis" style="left:840px">
    <div class="icon"><svg width="40" height="40" viewBox="0 0 40 40"><rect x="7" y="6" width="26" height="30" rx="2" fill="none" stroke="#2b2b2b" stroke-width="3"/><rect x="14" y="3" width="12" height="6" fill="#2b2b2b"/><path d="M13 21l5 5 9-10" fill="none" stroke="#2b2b2b" stroke-width="3"/></svg></div>
    <h3>Strict Liability</h3>
    <div class="card">There are certain cases where an injury victim does not have to specifically prove any of the forms of misconduct indicated above. When a defective product causes injury to a consumer..<div class="plus">+</div></div>
  </div>
</section>

<section class="compensation">
  <div class="comp-visual" role="img" aria-label="Personal injury compensation claim form with a gavel"></div>
  <h2 class="comp-title" style="font-weight:400">Seeking Significant Compensation for<br><span class="gold">Serious Injuries</span></h2>
  <div class="comp-text">
    <p>When you fall on a wet floor in a grocery store or you are struck in a crosswalk while walking across the street, you can suffer a wide range of injuries, including permanently debilitating injuries. When you suffer a catastrophic injury like a traumatic brain injury or spinal cord injury, the medical and supportive care costs can easily amount to hundreds of thousands or even a million dollars over an injury victim's lifetime. Mr. Vantholm draws on his proven success handling catastrophic injury cases and his established network of experts to obtain the fullest compensation for his clients.</p>
    <p>While the specific damages available in a personal injury lawsuit will depend on the precise facts and circumstances, some types of damages we might pursue include:</p>
  </div>
  <div class="damages">
    <span><svg width="14" height="14" viewBox="0 0 14 14"><rect x=".75" y=".75" width="12.5" height="12.5" fill="none" stroke="#b7811f" stroke-width="1.5"/><path d="M3 7l3 3 5-6" fill="none" stroke="#b7811f" stroke-width="2"/></svg>Lost income</span>
    <span><svg width="14" height="14" viewBox="0 0 14 14"><rect x=".75" y=".75" width="12.5" height="12.5" fill="none" stroke="#b7811f" stroke-width="1.5"/><path d="M3 7l3 3 5-6" fill="none" stroke="#b7811f" stroke-width="2"/></svg>Diminished earning</span>
    <span><svg width="14" height="14" viewBox="0 0 14 14"><rect x=".75" y=".75" width="12.5" height="12.5" fill="none" stroke="#b7811f" stroke-width="1.5"/><path d="M3 7l3 3 5-6" fill="none" stroke="#b7811f" stroke-width="2"/></svg>Impaired enjoyment</span>
    <span><svg width="14" height="14" viewBox="0 0 14 14"><rect x=".75" y=".75" width="12.5" height="12.5" fill="none" stroke="#b7811f" stroke-width="1.5"/><path d="M3 7l3 3 5-6" fill="none" stroke="#b7811f" stroke-width="2"/></svg>Medical expenses</span>
    <span><svg width="14" height="14" viewBox="0 0 14 14"><rect x=".75" y=".75" width="12.5" height="12.5" fill="none" stroke="#b7811f" stroke-width="1.5"/><path d="M3 7l3 3 5-6" fill="none" stroke="#b7811f" stroke-width="2"/></svg>Loss of companionship</span>
    <span><svg width="14" height="14" viewBox="0 0 14 14"><rect x=".75" y=".75" width="12.5" height="12.5" fill="none" stroke="#b7811f" stroke-width="1.5"/><path d="M3 7l3 3 5-6" fill="none" stroke="#b7811f" stroke-width="2"/></svg>Burial &amp; funeral costs</span>
    <span><svg width="14" height="14" viewBox="0 0 14 14"><rect x=".75" y=".75" width="12.5" height="12.5" fill="none" stroke="#b7811f" stroke-width="1.5"/><path d="M3 7l3 3 5-6" fill="none" stroke="#b7811f" stroke-width="2"/></svg>Pain &amp; suffering</span>
    <span><svg width="14" height="14" viewBox="0 0 14 14"><rect x=".75" y=".75" width="12.5" height="12.5" fill="none" stroke="#b7811f" stroke-width="1.5"/><path d="M3 7l3 3 5-6" fill="none" stroke="#b7811f" stroke-width="2"/></svg>Emotional distress</span>
    <span><svg width="14" height="14" viewBox="0 0 14 14"><rect x=".75" y=".75" width="12.5" height="12.5" fill="none" stroke="#b7811f" stroke-width="1.5"/><path d="M3 7l3 3 5-6" fill="none" stroke="#b7811f" stroke-width="2"/></svg>Punitive damages</span>
  </div>
</section>

<section class="attorneys">
  <h2 class="section-title" style="font-weight:400">Philadelphia Personal <span class="gold">Injury Attorneys</span></h2>
  <h4>Tenaciously Advocating for Injury Victims</h4>
  <p>Daniel R. Vantholm's success representing individuals who have suffered serious injury caused by negligent individuals, companies and government entities has twice merited his being awarded the status of Regional Rising Star by Top Counsel Review. Personal injury and wrongful death claims are subject to strict timing requirements and must be investigated promptly, so you should seek immediate legal advice if you are injured. Mr. Vantholm offers a no obligation free consultation to evaluate your case and advise you of your rights and options. Call Daniel Vantholm at 555-014-2270 to learn how we can help.</p>
</section>

<footer class="site-footer">
  <div class="foot-head" style="left:100px">QUICK LINKS</div>
  <div class="foot-rule" style="left:100px;width:310px"></div>
  <ul class="foot-links" style="left:100px"><li>Home</li><li>Slip and Fall</li><li>Auto Accident</li><li>Construction Injuries</li></ul>
  <ul class="foot-links" style="left:283px"><li>Medical Malpractice</li><li>Results</li><li>About Us</li><li>Contact Us</li></ul>
  <div class="foot-head" style="left:492px">CONTACT DETAILS</div>
  <div class="foot-rule" style="left:492px;width:205px"></div>
  <div class="foot-contact">
    <div class="row"><svg width="14" height="18" viewBox="0 0 14 18"><path d="M7 0a7 7 0 0 0-7 7c0 5 7 11 7 11s7-6 7-11a7 7 0 0 0-7-7z" fill="#d39c2c"/><circle cx="7" cy="7" r="2.5" fill="#6a0808"/></svg><div><b>DANIEL R. VANTHOLM</b><br>820 Harbor Row #410,<br>Eastport, ST 00000</div></div>
    <div class="row"><svg width="14" height="14" viewBox="0 0 24 24"><path d="M6.6 10.8a15 15 0 0 0 6.6 6.6l2.2-2.2c.3-.3.7-.4 1-.2 1.1.4 2.3.6 3.6.6.6 0 1 .4 1 1V20c0 .6-.4 1-1 1A17 17 0 0 1 3 4c0-.6.4-1 1-1h3.5c.6 0 1 .4 1 1 0 1.3.2 2.5.6 3.6.1.3 0 .7-.2 1z" fill="#d39c2c"/></svg><div>(555) 014-3381<br>(555) 014-2270</div></div>
    <div class="row"><svg width="14" height="11" viewBox="0 0 24 18"><rect x="1" y="1" width="22" height="16" fill="#d39c2c"/><path d="M1 1l11 9 11-9" fill="none" stroke="#6a0808" stroke-width="2"/></svg><div>inquiry@vantholmlegal.example</div></div>
  </div>
  <div class="foot-brand">
    <div class="name">Vantholm Injury Law Group</div>
    <div class="sub">DANIEL R. VANTHOLM, ESQUIRE</div>
    <div class="social"><span aria-label="Social profile"></span><span aria-label="Social profile"></span><span aria-label="Social profile"></span><span aria-label="Social profile"></span></div>
  </div>
</footer>
<div class="copyright">Copyright © 2016 Vantholmlegal. All Rights Reserved.</div>

</body>
</html>
```